Business card design and logo needed - Photographer

I take photos of weddings, rodeos, snowmobiling.
Need a card to hand out to prospective clients.
Industry/Entity Type
Business
Contact Information for Business Card
Marcus Dolven Photography
Requirements
Must have
- Bold
Black or white base.
My website. www.MarcusDolven.example
Should not have
- camera/ lens/ aperture blades

```html
<!DOCTYPE html>
<html lang="en">
<head>
<meta charset="utf-8">
<title>Marcus Dolven Photography – Business Cards</title>
<link rel="stylesheet" href="https://fonts.googleapis.com/css2?family=Archivo:wght@800&family=Cinzel:wght@400&display=swap">
<style>
  :root {
    --backdrop: #4d4d4d;
    --ink-black: #050607;
    --type-grey: #cbcbcc;
    --panel-light: #e7e7e7;
    --text-white: #ffffff;
    --sky-top: #1f3f8f;
    --sky-mid: #4f86c6;
    --sky-glow: #a9c9e4;
    --horizon: #e08a4a;
    --ground: #1c2418;
  }
  * { margin: 0; padding: 0; box-sizing: border-box; }
  html, body {
    width: 1200px; height: 900px; overflow: hidden;
    background: var(--backdrop);
  }
  .canvas { position: relative; width: 1200px; height: 900px; }

  .card { position: absolute; overflow: hidden; }

  /* Front card */
  .card--front { left: 150px; top: 70px; width: 620px; height: 354px; }
  .front__photo {
    position: absolute; inset: 0;
    background: linear-gradient(180deg,
      var(--sky-top) 0%, var(--sky-mid) 45%, var(--sky-glow) 66%,
      var(--horizon) 76%, #4a4630 80%, var(--ground) 86%, var(--ground) 100%);
  }
  .front__contact {
    position: absolute; top: 30px; right: 100px; text-align: right;
    font-family: "Cinzel", serif; color: var(--text-white);
    font-size: 11px; line-height: 1.65; letter-spacing: 0.3px;
  }
  .front__contact .studio { font-size: 13px; }
  .front__mark {
    position: absolute; top: 30px; right: 18px; width: 74px;
    font-family: "Cinzel", serif; font-size: 13px; line-height: 1.2;
    color: var(--type-grey); text-align: center;
  }
  .front__wordmark {
    position: absolute; left: 10px; right: 6px; bottom: -16px;
    white-space: nowrap;
    font-family: "Archivo", sans-serif; font-weight: 800;
    font-size: 84px; letter-spacing: -4px; color: var(--type-grey);
  }

  /* Back card */
  .card--back {
    left: 500px; top: 470px; width: 560px; height: 320px;
    background: var(--ink-black);
  }
  .back__panel {
    position: absolute; left: 0; top: 0; bottom: 0; width: 74px;
    background: var(--panel-light);
  }
  .back__name {
    position: absolute; left: 90px; top: 128px;
    font-family: "Archivo", sans-serif; font-weight: 800;
    font-size: 92px; line-height: 0.92; letter-spacing: -4px;
    color: var(--type-grey);
  }
  .back__contact {
    position: absolute; top: 22px; right: 26px; text-align: right;
    font-family: "Cinzel", serif; color: var(--text-white);
    font-size: 17px; line-height: 1.2;
  }
  .back__contact .phone { font-size: 14px; }
  .back__contact .web { font-size: 11px; margin-top: 4px; }
</style>
</head>
<body>
<main class="canvas">

  <section class="card card--front">
    <div class="front__photo" role="img" aria-label="Photograph of a twilight sky over a dark field with trees at the horizon"></div>
    <div class="front__contact">
      <div class="studio">Marcus Dolven Photography</div>
      <div>306.555.0142</div>
      <div>www.MarcusDolven.example</div>
      <div>www.social.example/marcus.dolven</div>
    </div>
    <div class="front__mark">Marcus Dolven</div>
    <div class="front__wordmark">MarcusDolven</div>
  </section>

  <section class="card card--back">
    <div class="back__panel"></div>
    <div class="back__name">Marcus<br>Dolven</div>
    <div class="back__contact">
      <div>Marcus Dolven</div>
      <div>Photography</div>
      <div class="phone">306.555.0142</div>
      <div class="web">www.MarcusDolven.example</div>
    </div>
  </section>

</main>
</body>
</html>
```